Outdoor banner - allegorical car (float) on Gay Pride

We need a graphics for advertising banner promoting web project www.spektrovia.com
Approximate size 120x40inch (3x1meters) - Therefore, it is required vector graphics, any embedded bitmaps in high resolution.

We launching new social network and city guide application for Prague visitors.
Keywords for poster are: city, Prague, traveling, rainbow, party, colors, holiday,..
It must contain the dominant text "SPEKTROVIA.COM".
Banner will be placed on an float (allegorical car) in the parade Prague Colour Parade 2014. And this banner will be the dominant car graphics.

- modern party look
- it should be understood that it is the queer(gay) web :)
- appropriate use of rainbow colors( or elements) in the graphics
- is possible to use silhouette of Prague

update:
- preferred is a vector graphics (vector elements)
- with regard to the size of the banner is not suitable the one big bitmap photo
- banner will be horizontal
Updates

update: - preferred is a vector graphics (vector elements) - with regard to the size of the banner is not suitable the one big bitmap photo

Target Market(s)

Prague visitors ..looking for entertainment., services..

Industry/Entity Type

Advertising

Requirements
Must have
• dominant text "SPEKTROVIA.COM"
rainbow colors( or elements) in the graphics
vector graphics for large format printing

```html
<!DOCTYPE html>
<html lang="en">
<head>
<meta charset="utf-8">
<title>Spektrovia.com – Parade Banner</title>
<link rel="stylesheet" href="https://fonts.googleapis.com/css2?family=Poppins:wght@700&display=swap">
<style>
  :root {
    --page: #ffffff;
    --ink: #000000;
    --red: #ff4a5c;
    --orange: #fbb46a;
    --yellow: #ffff5a;
    --green: #4cff5c;
    --blue: #4a5cf2;
    --purple: #b450f5;
    --light: #ffffff;
  }
  html, body {
    margin: 0;
    padding: 0;
    width: 1200px;
    height: 1000px;
    overflow: hidden;
    background: var(--page);
  }
  .canvas {
    position: relative;
    width: 1200px;
    height: 1000px;
  }
  .banner {
    position: absolute;
    left: 38px;
    top: 298px;
    width: 1124px;
    height: 375px;
    display: block;
  }
  .brand-name {
    font-family: "Poppins", Arial, sans-serif;
    font-weight: 700;
    fill: var(--ink);
  }
</style>
</head>
<body>
<main class="canvas">
  <svg class="banner" viewBox="0 0 1124 375" xmlns="http://www.w3.org/2000/svg">
    <defs>
      <linearGradient id="stripe-red" x1="0" y1="0" x2="0" y2="1">
        <stop offset="0" stop-color="var(--red)" stop-opacity="0.55"/>
        <stop offset="0.5" stop-color="var(--red)" stop-opacity="0.35"/>
        <stop offset="1" stop-color="var(--red)" stop-opacity="1"/>
      </linearGradient>
      <linearGradient id="stripe-orange" x1="0" y1="0" x2="0" y2="1">
        <stop offset="0" stop-color="var(--orange)" stop-opacity="1"/>
        <stop offset="0.55" stop-color="var(--orange)" stop-opacity="0.25"/>
        <stop offset="1" stop-color="var(--orange)" stop-opacity="0.9"/>
      </linearGradient>
      <linearGradient id="stripe-yellow" x1="0" y1="0" x2="0" y2="1">
        <stop offset="0" stop-color="var(--yellow)" stop-opacity="1"/>
        <stop offset="0.6" stop-color="var(--yellow)" stop-opacity="0.25"/>
        <stop offset="1" stop-color="var(--yellow)" stop-opacity="0.9"/>
      </linearGradient>
      <linearGradient id="stripe-green" x1="0" y1="0" x2="0" y2="1">
        <stop offset="0" stop-color="var(--green)" stop-opacity="1"/>
        <stop offset="0.6" stop-color="var(--green)" stop-opacity="0.15"/>
        <stop offset="1" stop-color="var(--green)" stop-opacity="0.75"/>
      </linearGradient>
      <linearGradient id="stripe-blue" x1="0" y1="0" x2="0" y2="1">
        <stop offset="0" stop-color="var(--blue)" stop-opacity="1"/>
        <stop offset="0.55" stop-color="var(--blue)" stop-opacity="0.2"/>
        <stop offset="1" stop-color="var(--blue)" stop-opacity="0.8"/>
      </linearGradient>
      <linearGradient id="stripe-purple" x1="0" y1="0" x2="0" y2="1">
        <stop offset="0" stop-color="var(--purple)" stop-opacity="0.45"/>
        <stop offset="0.5" stop-color="var(--purple)" stop-opacity="0.55"/>
        <stop offset="1" stop-color="var(--purple)" stop-opacity="1"/>
      </linearGradient>
      <radialGradient id="spotlight" cx="0.5" cy="0.5" r="0.5">
        <stop offset="0" stop-color="var(--light)" stop-opacity="1"/>
        <stop offset="1" stop-color="var(--light)" stop-opacity="0"/>
      </radialGradient>
      <radialGradient id="city-glow" cx="0.5" cy="0.5" r="0.5">
        <stop offset="0" stop-color="var(--light)" stop-opacity="0.9"/>
        <stop offset="0.7" stop-color="var(--light)" stop-opacity="0.55"/>
        <stop offset="1" stop-color="var(--light)" stop-opacity="0"/>
      </radialGradient>
    </defs>

    <g class="rainbow-stripes">
      <rect class="stripe stripe--red" x="0" y="0" width="188" height="375" fill="url(#stripe-red)"/>
      <rect class="stripe stripe--orange" x="187" y="0" width="188" height="375" fill="url(#stripe-orange)"/>
      <rect class="stripe stripe--yellow" x="374" y="0" width="188" height="375" fill="url(#stripe-yellow)"/>
      <rect class="stripe stripe--green" x="561" y="0" width="188" height="375" fill="url(#stripe-green)"/>
      <rect class="stripe stripe--blue" x="748" y="0" width="188" height="375" fill="url(#stripe-blue)"/>
      <rect class="stripe stripe--purple" x="936" y="0" width="188" height="375" fill="url(#stripe-purple)"/>
    </g>

    <g class="spotlights">
      <ellipse cx="40" cy="18" rx="70" ry="36" fill="url(#spotlight)"/>
      <ellipse cx="1084" cy="18" rx="70" ry="36" fill="url(#spotlight)"/>
    </g>

    <ellipse class="city-outline-area" role="img" aria-label="Outline map of the city boundary"
             cx="560" cy="185" rx="185" ry="140" fill="url(#city-glow)"/>

    <text class="brand-name" x="52" y="208" font-size="96"
          textLength="1020" lengthAdjust="spacing">Spektrovia.com</text>
  </svg>
</main>
</body>
</html>
```